A5 Patient Information Booklet (Chiropractic Clinic) 4-8 pages

Here’s a polished, professional rewrite of your full brief and content, with clearer structure, corrected language, and a premium tone:

---

**Project Title:** Premium Patient Information Brochure (Chiropractic & Wellness Clinic)

---

### **Overview**

We are a health and wellness clinic seeking a premium, high-end patient information brochure to provide following a patient’s initial consultation and first treatment.

The purpose of this booklet is to:

* Reinforce trust and professionalism
* Help patients understand what to expect next
* Encourage adherence to care recommendations
* Position the clinic as calm, expert-led, and results-driven

---

### **Format**

* 4–8 page booklet (A5 or similar size)
* Print-ready and digital versions required

---

### **Target Audience**

Patients who have just completed their initial consultation and may have begun treatment. They may already be experiencing physical or mental changes, so the brochure should guide, reassure, and educate them on what comes next.

---

### **Tone & Style**

* Premium, calm, and reassuring
* Modern wellness aesthetic (not overly clinical)
* Clean layout with minimal clutter
* Soft, neutral colour palette (whites, creams, muted greens, soft blues)
* Elegant typography (e.g. Montserrat / Lato)
* High-end, trustworthy, and professional feel

---

### **Key Messages**

#### 1. Listen to Your Body

Patients may feel different after treatment. Reassure them that this is normal and part of the healing process.

#### 2. Post-Treatment Advice

* Stay well hydrated
* Rest if needed
* Avoid overexertion if the body requires recovery

#### 3. Healing is a Journey (Core Concept)

A strong visual metaphor of a **“road to recovery”** or **journey** should be central to the design.

This journey should clearly illustrate three phases:

* **Phase 1: Initial Care (Weeks 1–6)**
Focus: Reducing pain/discomfort, calming the body, and initiating response to treatment

* **Phase 2: Corrective Care (Weeks 6–12)**
Focus: Addressing underlying issues, improving function, and creating lasting change

* **Phase 3: Wellness / Maintenance (Ongoing)**
Focus: Maintaining progress, preventing relapse, and supporting long-term wellbeing

**Important:**

* Emphasise that this is not a quick fix
* Progress requires time and consistency
* Each patient follows an individualised care plan
* The journey should feel structured, positive, and achievable

#### 4. Personalised Care

Reinforce that every treatment plan is tailored specifically to the individual.

#### 5. Professional Reassurance

Patients should feel confident they are in expert hands and supported throughout their journey.

---

### **Design Direction**

* Use imagery that reflects calmness, progression, and wellness (e.g. pathways, nature, soft gradients)
* Avoid generic stock imagery
* **Only use original clinic images from website and social media**
* Prioritise white space and clarity
* Aim for a luxury spa/medical hybrid aesthetic

---

## **Content Structure (Page-by-Page)**

### **Front Cover**

* Clean, minimal, premium design
* Clinic branding

---

### **Page 1: Patient Case Summary**

**Title:** *Welcome to Fernwell Practice*

Thank you for choosing Fernwell Practice.

This booklet is designed to guide you through:

* What we found during your initial consultation
* Your personalised recommended treatment plan
* Your road to recovery
* Long-term wellness care
* Why we take the approach we do

---

### **Page 2: Your Care Journey**

**Stage 1: Your Initial Consultation**

Today we completed a comprehensive assessment of your health and function, including:

* Full case history and discussion of your symptoms and goals
* Orthopaedic and neurological testing
* Postural and movement assessment
* Initial treatment (where appropriate)

**What this tells us:**

* How your body is currently functioning
* Where areas of stress or dysfunction may be present
* The most appropriate and effective path forward for your care

---

### **Page 3: Your Suggested Treatment Plan**

Based on today’s findings, your recommended care plan is:

**______ treatments over ______ weeks**

This should be viewed alongside your *Road to Recovery* to help you understand what to expect.

We have also discussed:

* Expected timelines for improvement
* Available payment options

**After Treatment:**
It is common to feel different following treatment. This is a normal response as your body begins to adapt and respond.

We recommend:

* Staying well hydrated
* Allowing time for rest and recovery
* Avoiding overexertion if your body feels it needs it

---

### **Page 4: What to Expect Next**

Healing is not always linear—it is a process that occurs over time.

Your care will typically progress through the following stages:

* **Relief Care**
Focused on reducing discomfort and calming the body

* **Corrective Care**
Focused on addressing underlying issues and improving function
(This phase may include prescribed exercises)

* **Maintenance / Wellness Care**
Focused on sustaining progress, preventing recurrence, and supporting long-term health

---

### **Page 5: Understanding Chiropractic Care**

**What is Chiropractic?**
Chiropractic care focuses on the relationship between the spine, nervous system, and overall body function.

By improving spinal movement and alignment, chiropractic care helps support the nervous system, allowing the body to function and heal more effectively.

**About Fernwell Practice**
At Fernwell Practice, our approach is centred around personalised, patient-focused care. We aim to not only relieve symptoms but to address underlying causes and support long-term wellbeing.

---

### **Back Page**

* Clinic contact details
* Website
* Social media icons/handles

**Closing Message:**
“A healthier, stronger you—supported every step of the way.”

---

### **Deliverables**

* Print-ready PDF
* Editable source files

---

### **Additional Notes**

* The brochure should feel valuable and worth keeping
* Encourage long-term care in a subtle, non-pushy way
* Maintain clarity, readability, and strong visual hierarchy
* Balance professionalism with warmth and approachability

---

If you’d like, I can also turn this into **actual brochure copy (fully written, patient-facing text)** or help you refine it further for a designer.

Target Market(s)

Existing patients who want to feel better and look after themselves that is given after their initil consultation appointment

Industry/Entity Type

Chiropractic, wellness, health

Font styles to use
Other font styles liked:
• Montserrat or Lato

Colors
0094D4
00A9DD
6FCCEA
C7EBF8
E9F6FB
00AB8E
00BBA5
67D7C9
C6EFE9
E9F9F6
6B429C
8869AF
B7A5CE
E3DAEB
F3F0F8

Requirements
Must have
• my own photos, look premium wellness, be clear and simple to understand for patients journey or what to expect next and over time
Nice to have
• USe my social media/website for ideas
Should not have
• generic photos and images

```html
<!DOCTYPE html>
<html lang="en">
<head>
<meta charset="utf-8">
<title>Fernwell Practice – Patient Booklet</title>
<link rel="stylesheet" href="https://fonts.googleapis.com/css2?family=Playfair+Display:wght@400;500;600&family=Montserrat:ital,wght@0,400;0,500;0,600;0,700;1,400&family=Mrs+Saint+Delafield&display=swap">
<style>
:root{
  --board:#3d4350;
  --paper:#ffffff;
  --ink:#2e5b5a;
  --text:#2f3a3a;
  --teal:#1fa39a;
  --teal-soft:#e3f6f3;
  --purple:#8a68ae;
  --blue:#3d8fc4;
  --muted:#6b7474;
}
*{box-sizing:border-box;margin:0;padding:0}
html,body{width:1200px;height:2286px;overflow:hidden;background:var(--board)}
body{position:relative;font-family:'Montserrat',sans-serif;color:var(--text)}
.page{position:absolute;width:481px;height:682px;background:var(--paper);overflow:hidden}
.col-l{left:116px}.col-r{left:604px}
.row-1{top:113px}.row-2{top:803px}.row-3{top:1492px}
.abs{position:absolute}
.serif{font-family:'Playfair Display',serif}
.script{font-family:'Mrs Saint Delafield',cursive}
.center{left:0;right:0;text-align:center}
.photo{position:absolute}
.brand-mark{position:absolute;border:3px solid var(--teal);border-radius:50%}
.brand-name{font-family:'Montserrat',sans-serif;font-weight:600;color:#2b2b2b;letter-spacing:.5px}
.brand-sub{font-size:8.5px;letter-spacing:2px;color:var(--teal);font-weight:500}

/* cover */
.cover-photo{inset:0;background:linear-gradient(160deg,#f3ead9 0%,#e2c9a6 35%,#b88a62 65%,#4a3428 100%)}
.cover-title{left:28px;top:180px;font-size:38px;line-height:35px;color:var(--ink);font-weight:600}
.cover-script{color:#fff;font-size:40px;line-height:1}
.cover-tag{left:28px;top:384px;width:76px;font-size:11.5px;line-height:18px;color:#fff}

/* body copy */
.copy{font-size:9.5px;line-height:16.5px;color:var(--text)}
.copy strong{color:var(--ink);font-weight:600}
.quote-box{background:var(--teal-soft);font-size:9.5px;font-style:italic;color:var(--ink);display:flex;align-items:center;justify-content:center}
.h-page{color:var(--ink);font-family:'Playfair Display',serif;font-weight:500}
.divider{position:absolute;height:1px;background:var(--teal);left:120px;width:240px}
.leaf-dot{position:absolute;width:8px;height:14px;border-radius:50%;background:var(--teal);left:236px}
.icon-disc{position:absolute;width:28px;height:28px;border-radius:50%;background:var(--ink)}
.h-step{font-weight:700;font-size:19px;color:var(--ink);line-height:27px}
.subhead{font-weight:600;color:var(--teal);font-size:9.5px}
.checks{list-style:none;font-size:8.5px;line-height:16px}
.checks li{position:relative;padding-left:13px}
.checks li::before{content:"";position:absolute;left:0;top:5px;width:6px;height:6px;border-radius:50%;background:var(--teal)}
.care-row{position:absolute;left:164px;font-size:8.5px;line-height:16px;display:flex;gap:12px}
.care-row i{width:14px;height:10px;background:var(--teal);border-radius:2px;margin-top:3px;flex:none}

/* journey */
.road-art{left:30px;top:230px;width:420px;height:380px;background:radial-gradient(ellipse at 55% 45%,rgba(198,239,233,.75) 0%,rgba(227,218,235,.5) 45%,rgba(255,255,255,0) 72%)}
.phase-title{font-weight:700;font-size:19px;line-height:22px}
.phase-sub{font-size:8.5px;font-weight:600}
.badge{display:inline-block;color:#fff;font-size:8px;font-weight:700;padding:1px 6px;border-radius:8px;margin-top:4px}
.bullets{list-style:none;font-size:8.5px;line-height:14px;margin-top:5px}
.bullets li{position:relative;padding-left:9px}
.bullets li::before{content:"•";position:absolute;left:0;color:var(--teal)}
.p1{color:var(--teal)}.p2{color:var(--purple)}.p3{color:var(--blue)}

/* care plan */
.form-head{left:41px;width:411px;top:149px;height:19px;background:var(--teal-soft);display:flex;justify-content:space-between;align-items:center;padding:0 12px;font-size:7px}
.form-head b{color:var(--ink);font-weight:700}
.form-head em{color:var(--muted)}
.form-box{left:41px;width:411px;top:171px;height:111px;border:1px solid var(--teal)}
.field{position:absolute;left:12px;right:0;font-size:7px;display:flex;align-items:flex-end;gap:2px}
.field span.line{flex:1;border-bottom:1px solid var(--teal);height:10px}
.pillar{position:absolute;width:110px;text-align:center}
.pillar .ico{width:18px;height:18px;margin:0 auto;background:var(--teal);border-radius:4px}
.pillar h4{font-size:10px;font-weight:700;color:var(--teal);line-height:17px;margin-top:10px}
.pillar hr{border:0;border-top:1px solid #bcd;width:80px;margin:10px auto 8px}
.pillar p{font-size:7px;line-height:12px;color:var(--muted)}
.step{position:absolute;display:flex;gap:6px;width:130px}
.step .num{width:16px;height:16px;border-radius:50%;background:#2b2b2b;color:#fff;font-size:9px;font-weight:700;display:flex;align-items:center;justify-content:center;flex:none}
.step .ico{width:20px;height:22px;border:2px solid #444;border-radius:3px;flex:none}
.step h5{font-size:9.5px;color:var(--teal);font-weight:700;line-height:13px}
.step p{font-size:7px;line-height:12px;color:var(--muted);margin-top:2px}

/* back */
.contact{position:absolute;left:45px;font-size:9.5px;line-height:16px;display:flex;gap:14px}
.contact i{width:10px;height:10px;border-radius:50%;background:var(--teal);flex:none;margin-top:3px}
.social{position:absolute;width:14px;height:14px;border-radius:50%;background:var(--teal)}
</style>
</head>
<body>

<!-- Cover -->
<section class="page col-l row-1">
  <div class="photo cover-photo" role="img" aria-label="Photo of a chiropractor gently adjusting a relaxed patient's neck in a warm, sunlit treatment room"></div>
  <div class="brand-mark" style="left:195px;top:30px;width:90px;height:90px"></div>
  <div class="abs center brand-name" style="top:130px;font-size:19px">FERNWELL PRACTICE</div>
  <div class="abs center brand-sub" style="top:155px">CHIROPRACTIC &amp; WELLNESS</div>
  <h1 class="abs serif cover-title">Your Journey<br>to<br>Better<br>Health</h1>
  <div class="abs script cover-script" style="left:28px;top:332px">Starts Here</div>
  <div class="abs" style="left:28px;top:374px;width:180px;height:1px;background:rgba(255,255,255,.7)"></div>
  <p class="abs cover-tag">Chiropractic &amp; Wellness Care, Tailored to You</p>
  <div class="abs script cover-script" style="left:290px;top:612px;font-size:34px;line-height:30px">You're in the<br>right place.</div>
</section>

<!-- What is chiropractic -->
<section class="page col-r row-1">
  <h2 class="abs h-page" style="left:149px;top:40px;font-size:26px;line-height:31px">What is<br>Chiropractic Care?</h2>
  <p class="abs copy" style="left:149px;top:155px;width:255px"><strong>Chiropractic</strong> care focuses on how your body moves, functions, and heals as a whole.</p>
  <p class="abs copy" style="left:152px;top:208px;width:250px">By improving alignment and mobility of the spine and joints, we help reduce tension on the nervous system—supporting your body's natural ability to adapt, recover, and function at its best.</p>
  <div class="photo" style="left:0;top:204px;width:122px;height:333px;background:linear-gradient(90deg,#c7a88d 0%,#dfe8ef 70%,#ffffff 100%)" role="img" aria-label="Portrait of the practice's chiropractor smiling"></div>
  <div class="abs" style="left:254px;top:305px;width:40px;height:40px;border:2px solid var(--teal);border-radius:50%"></div>
  <p class="abs copy" style="left:149px;top:375px;width:255px;text-align:justify"><strong>At Fernwell Practice,</strong> care is personalised to you. We take time to understand your lifestyle, your goals, and how your body is responding. Your care may support: Reducing pain and discomfort Improving movement and flexibility Supporting nervous system regulation Enhancing overall wellbeing Rather than simply managing symptoms, our focus is long-term health—helping you feel, move, and live better.</p>
  <div class="abs quote-box" style="left:71px;top:591px;width:338px;height:38px">Care that supports your body—not just your symptoms.</div>
</section>

<!-- What to expect -->
<section class="page col-l row-2">
  <h2 class="abs center h-page" style="top:42px;font-size:24px;line-height:30px">What to Expect<br>After Your Treatment</h2>
  <div class="divider" style="top:122px"></div><div class="leaf-dot" style="top:115px"></div>
  <div class="icon-disc" style="left:121px;top:146px"></div>
  <h3 class="abs h-step" style="left:164px;top:146px">1. Listen to Your Body</h3>
  <p class="abs copy" style="left:164px;top:180px;width:180px;font-size:8.5px">After your treatment, it's normal to feel different. Your body is beginning to respond, adapt, and heal.</p>
  <p class="abs subhead" style="left:164px;top:240px">You may notice:</p>
  <ul class="abs checks" style="left:164px;top:266px;width:160px">
    <li>Mild soreness or stiffness Increased awareness in certain areas</li>
    <li>A sense of release or fatigue</li>
    <li>This is all part of the process.</li>
  </ul>
  <div class="divider" style="top:367px"></div><div class="leaf-dot" style="top:360px"></div>
  <div class="photo" style="left:0;top:400px;width:150px;height:282px;background:linear-gradient(90deg,#c9b5a3 0%,#e8e4e4 60%,#ffffff 100%)" role="img" aria-label="Chiropractor treating a seated patient's shoulder"></div>
  <div class="icon-disc" style="left:121px;top:393px"></div>
  <h3 class="abs h-step" style="left:164px;top:390px">2. Support Your<br>Recovery</h3>
  <div class="care-row" style="top:460px"><i></i><span>Stay well hydrated</span></div>
  <div class="care-row" style="top:488px"><i></i><span>Allow your body time to rest</span></div>
  <div class="care-row" style="top:516px"><i></i><span>Avoid overexertion if you feel you<br>need recovery</span></div>
  <div class="icon-disc" style="left:121px;top:591px"></div>
  <div class="abs quote-box" style="left:153px;top:585px;width:227px;height:38px;font-style:normal;justify-content:flex-start;padding-left:12px;font-size:9.5px;line-height:15px;color:var(--text)">Your body knows how to heal —we're here<br>to guide it.</div>
</section>

<!-- Recovery journey -->
<section class="page col-r row-2">
  <div class="photo road-art" role="img" aria-label="Soft teal and lilac illustration of a winding road representing the recovery journey"></div>
  <h2 class="abs center h-page" style="top:42px;font-size:24px;line-height:26px">Your Recovery</h2>
  <div class="abs center h-page" style="top:64px;font-size:42px;font-weight:600;line-height:46px">Journey</div>
  <p class="abs center" style="top:126px;font-size:10px;color:var(--muted)">Healing is a process — structured, personal, and progressive.</p>

  <div class="abs" style="left:96px;top:168px;width:24px;height:20px;border:2px solid var(--teal);border-radius:12px 12px 2px 2px"></div>
  <div class="abs" style="left:135px;top:162px">
    <div class="phase-title p1">PHASE 1</div>
    <div class="phase-sub p1">Initial Care</div>
    <span class="badge" style="background:var(--teal)">WEEKS 1-6</span>
    <ul class="bullets"><li>Reducing pain and discomfort</li><li>Calming the nervous system</li><li>Helping your body begin<br>to respond</li></ul>
  </div>

  <svg class="abs" style="left:214px;top:310px" width="28" height="22" aria-hidden="true"><path d="M1 21 L11 3 L17 12 L20 8 L27 21 Z" fill="none" stroke="#8a68ae" stroke-width="2"/></svg>
  <div class="abs" style="left:255px;top:302px">
    <div class="phase-title p2">PHASE 2</div>
    <div class="phase-sub p2">Corrective Care</div>
    <span class="badge" style="background:var(--purple)">WEEKS 6-12</span>
    <ul class="bullets"><li>Addressing underlying issues</li><li>Improving movement<br>and function</li><li>Creating lasting structural<br>change</li></ul>
  </div>

  <svg class="abs" style="left:214px;top:460px" width="26" height="32" aria-hidden="true"><circle cx="13" cy="5" r="4" fill="none" stroke="#3d8fc4" stroke-width="2"/><path d="M2 10 L13 14 L24 10 M13 14 V22 M13 22 L8 31 M13 22 L18 31" fill="none" stroke="#3d8fc4" stroke-width="2"/></svg>
  <div class="abs" style="left:255px;top:455px">
    <div class="phase-title p3">PHASE 3</div>
    <div class="phase-sub p3">Wellness / Maintenance</div>
    <span class="badge" style="background:var(--blue)">ONGOING</span>
    <ul class="bullets"><li>Maintaining progress</li><li>Preventing relapse</li><li>Supporting overall<br>wellbeing</li></ul>
  </div>

  <p class="abs center" style="top:596px;font-size:10px">This is not a quick fix.</p>
  <p class="abs center" style="top:613px;font-size:10px">True healing takes consistency, time, and the right guidance.</p>
  <p class="abs center" style="top:632px;font-size:10px;font-style:italic;color:var(--teal)">Every journey is different — your care plan is tailored specifically to you.</p>
</section>

<!-- Care plan -->
<section class="page col-l row-3">
  <h2 class="abs center h-page" style="top:42px;font-size:24px;line-height:26px">Your Personalised</h2>
  <div class="abs center h-page" style="top:64px;font-size:40px;font-weight:600;line-height:44px">Care Plan</div>
  <p class="abs center" style="top:125px;font-size:10px">Designed specifically for your body, your goals, and your lifestyle</p>
  <div class="abs form-head"><b>PATIENT INFORMATION</b><em>Your plan, your progress, your results.</em></div>
  <div class="abs form-box">
    <div class="field" style="top:12px">Full Name:<span class="line"></span></div>
    <div class="field" style="top:39px">Treatments Over:<span class="line"></span></div>
    <div class="field" style="top:66px"><span class="line"></span></div>
    <div class="field" style="top:95px">Weeks:</div>
  </div>
  <div class="pillar" style="left:60px;top:310px"><div class="ico" style="border-radius:50% 50% 3px 3px"></div><h4>Personalised<br>Approach</h4><hr><p>Care that's<br>tailored to you</p></div>
  <div class="pillar" style="left:185px;top:310px"><div class="ico" style="border-radius:3px 3px 50% 50%"></div><h4>Evidence-Informed<br>Care</h4><hr><p>Safe, effective,<br>and professional</p></div>
  <div class="pillar" style="left:313px;top:310px"><div class="ico" style="border-radius:50%"></div><h4>Ongoing<br>Support</h4><hr><p>We're with you<br>for the long term</p></div>
  <h3 class="abs center h-page" style="top:434px;font-size:25px;line-height:30px">You don't have to live with pain.<br>Start feeling better today</h3>
  <p class="abs center" style="top:504px;font-size:9.5px;font-weight:600;color:var(--teal)">TAKE THE NEXT STEP</p>
  <div class="step" style="left:42px;top:540px"><span class="num">1</span><span class="ico"></span><div><h5>Book<br>your next<br>appointment</h5><p>Secure your next<br>session and stay<br>on track.</p></div></div>
  <div class="step" style="left:180px;top:540px"><span class="num">2</span><span class="ico"></span><div><h5>Follow<br>your<br>care plan</h5><p>Follow your<br>recommended<br>treatment schedule.</p></div></div>
  <div class="step" style="left:318px;top:540px"><span class="num">3</span><span class="ico" style="border-radius:50% 50% 3px 3px"></span><div><h5>Check in<br>with your<br>practitioner</h5><p>We'll review your<br>progress and<br>adjust as needed.</p></div></div>
</section>

<!-- Back page -->
<section class="page col-r row-3">
  <div class="brand-mark" style="left:195px;top:32px;width:90px;height:90px"></div>
  <div class="abs center brand-name" style="top:132px;font-size:19px">FERNWELL PRACTICE</div>
  <div class="abs center brand-sub" style="top:157px">CHIROPRACTIC &amp; WELLNESS</div>
  <h2 class="abs center h-page" style="top:178px;font-size:26px;line-height:31px">We're Here for You<br>Every Step of the Way</h2>
  <div class="photo" style="left:0;top:245px;width:481px;height:270px;background:linear-gradient(180deg,#ffffff 0%,#f1e2cc 20%,#e3c4a0 55%,#f4e9dc 85%,#ffffff 100%)" role="img" aria-label="Chiropractor examining a patient's back in a bright, calm clinic room"></div>
  <div class="contact" style="top:522px"><i></i><span>Fernwell Practice Chiropractic &amp; Wellness<br>12 Mill Lane, Ashbury AB1 2CD</span></div>
  <div class="contact" style="top:567px"><i style="border-radius:2px"></i><span>info@fernwellpractice.com</span></div>
  <div class="contact" style="top:592px"><i></i><span>www.fernwellpractice.com</span></div>
  <div class="abs" style="left:304px;top:525px;width:1px;height:85px;background:var(--ink)"></div>
  <div class="abs script" style="left:328px;top:530px;font-size:28px;color:var(--muted)">Follow Us</div>
  <div class="social" style="left:340px;top:584px"></div>
  <div class="social" style="left:383px;top:584px"></div>
  <p class="abs center script" style="top:628px;font-size:27px;color:var(--muted)">Feel better. Move better. Live better. — Naturally.</p>
</section>

</body>
</html>
```